Spino-Tarla
business card/ stationary
Spino-Tarla - Health
Creative Brief
Professional
Dr. Martin Pettigrew
Chiropractic Physician, CHO
914 Halden Rd Marlow Cove, CA 92318
mpw@spino-tarla.example
www.spino-tarla.example
use small logo as bullet for back of business card info. line 1 Health - Happiness - Abundance then bullets
Health - Happiness - Abundance - Natural Chiropractic Care: family wellness, chronic pain relief, personal injury - Ayurvedic Consultation: conscious lifestyle programs for stress management, nutrition, weight loss, physical and emotional balance - Quiet Current Stillness Practice: group and private instruction - Wellbeing Educational Seminars

```html
<!DOCTYPE html>
<html lang="en">
<head>
<meta charset="utf-8">
<title>Spino-Tarla – Business Card</title>
<link rel="stylesheet" href="https://fonts.googleapis.com/css2?family=Cinzel:wght@400;600;700&display=swap">
<style>
  :root {
    --backdrop: #f1ede6;
    --card-light: #eaf3d2;
    --card-mid: #dcebb6;
    --card-edge: #c9dc9c;
    --leaf-green: #7fae3a;
    --leaf-deep: #4f8a22;
    --ink-brown: #3d3a2a;
    --ink-blue: #2a6aa8;
    --bloom: #e88a3a;
  }
  * { margin: 0; padding: 0; box-sizing: border-box; }
  html, body { width: 1200px; height: 1009px; overflow: hidden; }
  body {
    background: var(--backdrop);
    font-family: "Cinzel", "Times New Roman", serif;
    color: var(--ink-brown);
    position: relative;
  }
  .card {
    position: absolute;
    width: 680px;
    height: 390px;
    border-radius: 26px;
    background: radial-gradient(ellipse at 60% 40%, var(--card-light) 0%, var(--card-mid) 100%);
    border: 1px solid var(--card-edge);
    box-shadow: 0 6px 18px rgba(60, 60, 30, 0.18);
    overflow: hidden;
  }
  .card--front { left: 60px; top: 60px; }
  .card--back { left: 460px; top: 560px; }

  .grass-accent {
    position: absolute;
    left: 26px;
    top: 30px;
    width: 34px;
    height: 340px;
    border-radius: 40% 40% 10% 10%;
    background: linear-gradient(180deg, rgba(127,174,58,0) 0%, rgba(127,174,58,0.55) 40%, rgba(79,138,34,0.8) 100%);
  }

  /* Front */
  .brand {
    position: absolute;
    left: 70px;
    top: 70px;
    width: 310px;
    text-align: center;
  }
  .brand__mark {
    display: block;
    margin: 0 auto 16px;
    width: 46px;
    height: 46px;
    border-radius: 50%;
    background: var(--bloom);
  }
  .brand__name {
    font-size: 36px;
    font-weight: 700;
    color: var(--leaf-deep);
    letter-spacing: 1px;
    line-height: 1;
    white-space: nowrap;
  }
  .practitioner {
    position: absolute;
    left: 120px;
    top: 270px;
  }
  .practitioner__name { font-size: 19px; color: var(--ink-brown); }
  .practitioner__role { font-size: 14px; margin-top: 6px; }

  .contact {
    position: absolute;
    left: 410px;
    top: 58px;
    font-size: 14px;
    line-height: 21px;
    color: var(--ink-brown);
  }
  .contact__group + .contact__group { margin-top: 20px; }
  .contact__address { margin-top: 54px; }

  /* Back */
  .motto {
    position: absolute;
    left: 0;
    top: 100px;
    width: 100%;
    text-align: center;
    font-size: 22px;
    font-weight: 400;
    color: var(--ink-brown);
    letter-spacing: 1px;
  }
  .motto__initial { color: var(--ink-blue); font-size: 28px; }
  .motto__word + .motto__word { margin-left: 14px; }

  .services {
    position: absolute;
    left: 140px;
    top: 172px;
    list-style: none;
    font-size: 14px;
    line-height: 19px;
  }
  .services__item {
    position: relative;
    padding-left: 22px;
    margin-bottom: 10px;
  }
  .services__item::before {
    content: "";
    position: absolute;
    left: 0;
    top: 4px;
    width: 11px;
    height: 11px;
    border-radius: 50%;
    background: var(--bloom);
  }
  .services__title { font-weight: 700; }
  .services__detail { font-size: 12px; display: block; }
</style>
</head>
<body>

  <section class="card card--front">
    <div class="grass-accent" role="img" aria-label="Slender green grass blade accent along the left edge"></div>

    <div class="brand">
      <span class="brand__mark"></span>
      <div class="brand__name">SPINO-TARLA</div>
    </div>

    <div class="practitioner">
      <div class="practitioner__name">DR. MARTIN PETTIGREW</div>
      <div class="practitioner__role">Chiropractic Physician, CHO</div>
    </div>

    <div class="contact">
      <div class="contact__group">
        T. (555) 214-7730<br>
        P. (555) 214-7730<br>
        C. (555) 214-7730<br>
        F. (555) 214-7730
      </div>
      <div class="contact__group">
        E. MPW@SPINO-TARLA.EXAMPLE<br>
        W. WWW.SPINO-TARLA.EXAMPLE<br>
        LICENSE NO. #470915
      </div>
      <div class="contact__group contact__address">
        914 HALDEN RD<br>
        MARLOW COVE, CA 92318
      </div>
    </div>
  </section>

  <section class="card card--back">
    <div class="grass-accent" role="img" aria-label="Slender green grass blade accent along the left edge"></div>

    <h2 class="motto">
      <span class="motto__word"><span class="motto__initial">H</span>EALTH</span>
      <span class="motto__word"><span class="motto__initial">H</span>APPINESS</span>
      <span class="motto__word"><span class="motto__initial">A</span>BUNDANCE</span>
    </h2>

    <ul class="services">
      <li class="services__item">
        <span class="services__title">Natural Chiropractic Care :</span>
        <span class="services__detail">family wellness, chronic pain relief, personal injury</span>
      </li>
      <li class="services__item">
        <span class="services__title">Ayurvedic Consultation :</span>
        <span class="services__detail">conscious lifestyle programs for stress management,<br>nutrition, weight loss, physical and emotional balance</span>
      </li>
      <li class="services__item">
        <span class="services__title">Quiet Current Stillness Practice :</span>
        <span class="services__detail">group and private instruction</span>
      </li>
      <li class="services__item">
        <span class="services__title">Wellbeing Educational Seminars</span>
      </li>
    </ul>
  </section>

</body>
</html>
```